Property developer, money partner needs business card design using logo concept provided

Our company develops residential properties, does money lends for joint ventures in property deals and finds property deals for other money partners. We have provided a basic logo for you to work from. Any graphic or logo design on the card is to communicate development and finance collaboration. Color choice is not so important for us, but color choice does need to reflect professionalism.

```html
<!DOCTYPE html>
<html lang="en">
<head>
<meta charset="utf-8">
<title>Brightlot Property Partners – Business Card</title>
<link rel="stylesheet" href="https://fonts.googleapis.com/css2?family=Open+Sans:wght@400;600;700&display=swap">
<style>
  :root {
    --backdrop: #2b2b2e;
    --card: #1e1d21;
    --card-edge: #141316;
    --ink: #f2f2f2;
    --muted: #b9b9bd;
    --red: #b3181d;
    --blue: #1c67c6;
    --mark-shade: #18171b;
  }
  * { box-sizing: border-box; margin: 0; padding: 0; }
  html, body { width: 1200px; height: 780px; overflow: hidden; }
  body {
    background: var(--backdrop);
    font-family: "Open Sans", Arial, sans-serif;
    color: var(--ink);
    position: relative;
  }
  .card {
    position: absolute;
    top: 230px;
    width: 525px;
    height: 300px;
    background: var(--card);
    border-radius: 4px;
    box-shadow: 0 6px 0 var(--card-edge), 0 18px 30px rgba(0,0,0,.45);
    overflow: hidden;
  }
  .card--front { left: 50px; }
  .card--back { left: 625px; }

  /* front */
  .watermark {
    position: absolute;
    right: 70px; bottom: -80px;
    width: 210px; height: 210px;
    border-radius: 50%;
    background: var(--mark-shade);
    z-index: 0;
  }
  .brand {
    position: absolute;
    display: flex;
    align-items: center;
    gap: 8px;
    z-index: 1;
  }
  .brand__dot {
    width: 14px; height: 14px;
    border-radius: 50%;
    background: var(--blue);
    flex: none;
  }
  .brand__name {
    font-weight: 700;
    color: var(--blue);
    letter-spacing: .04em;
    white-space: nowrap;
  }
  .card--front .brand { left: 34px; top: 30px; }
  .card--front .brand__name { font-size: 16px; }
  .acn { font-size: 8px; color: var(--muted); letter-spacing: .15em; }
  .card--front .acn { position: absolute; left: 56px; top: 56px; z-index: 1; }

  .contact {
    position: absolute;
    left: 34px;
    top: 96px;
    font-size: 14px;
    line-height: 1.45;
    z-index: 1;
  }
  .contact__address { margin-bottom: 10px; }
  .contact__row { display: flex; align-items: center; gap: 8px; }
  .contact__icon { width: 12px; height: 12px; flex: none; }

  .person {
    position: absolute;
    right: 40px;
    top: 196px;
    text-align: right;
    z-index: 1;
  }
  .person__name { font-size: 28px; font-weight: 700; line-height: 1.1; white-space: nowrap; }
  .person__first { color: var(--red); }
  .person__last { color: var(--blue); }
  .person__role { font-size: 15px; font-weight: 600; margin-top: 6px; }

  .accent-band {
    position: absolute;
    right: 0; top: 204px;
    width: 10px; height: 60px;
    background: var(--red);
    z-index: 1;
  }

  /* back */
  .card--back .brand-block {
    position: absolute;
    inset: 0;
    display: flex;
    flex-direction: column;
    align-items: center;
    justify-content: center;
    gap: 10px;
  }
  .card--back .brand { position: static; }
  .card--back .brand__dot { width: 22px; height: 22px; }
  .card--back .brand__name { font-size: 26px; }
  .card--back .acn { font-size: 10px; }
</style>
</head>
<body>
  <section class="card card--front" aria-label="Card front">
    <span class="watermark"></span>
    <div class="brand">
      <span class="brand__dot"></span>
      <span class="brand__name">Brightlot Property Partners</span>
    </div>
    <p class="acn">A.C.N 000 418 552</p>

    <div class="contact">
      <p class="contact__address">418 Elmridge Ave. Suite 310<br>Dallas, TX 75201</p>
      <p class="contact__row">
        <svg class="contact__icon" viewBox="0 0 12 12"><path d="M2 1h3l1 3-1.5 1a6 6 0 0 0 2.5 2.5L8 6l3 1v3a1 1 0 0 1-1 1A9 9 0 0 1 1 2a1 1 0 0 1 1-1z" fill="var(--red)"/></svg>
        (555) 214-6083
      </p>
      <p class="contact__row">
        <svg class="contact__icon" viewBox="0 0 12 12"><rect x="1" y="2.5" width="10" height="7" rx="1" fill="var(--red)"/><path d="M1.5 3l4.5 3.5L10.5 3" stroke="var(--card)" fill="none"/></svg>
        hello@brightlotpartners.com
      </p>
      <p class="contact__row">
        <svg class="contact__icon" viewBox="0 0 12 12"><circle cx="6" cy="6" r="5" fill="var(--red)"/><path d="M1 6h10M6 1c-2 2.5-2 7.5 0 10M6 1c2 2.5 2 7.5 0 10" stroke="var(--card)" stroke-width=".8" fill="none"/></svg>
        www.brightlotpartners.com
      </p>
    </div>

    <div class="person">
      <p class="person__name"><span class="person__first">Marta</span> <span class="person__last">Kovalenko</span></p>
      <p class="person__role">Managing Director</p>
    </div>
    <span class="accent-band"></span>
  </section>

  <section class="card card--back" aria-label="Card back">
    <div class="brand-block">
      <div class="brand">
        <span class="brand__dot"></span>
        <span class="brand__name">Brightlot Property Partners</span>
      </div>
      <p class="acn">A.C.N 000 418 552</p>
    </div>
  </section>
</body>
</html>
```